Business Card Design Project Lend Aid

Simple and clean business card,

Logo and fond added in attachment

Data need to be changable:
Ria Vondeck
Customer Service Specialist

Lend Aid - ria.vondeck@lendaid.be - Mob: +32491532876 - www.lendaid.be

Target Market(s)

Small businesses

Industry/Entity Type

Business

Requirements
Nice to have
• QR-code

```html
<!DOCTYPE html>
<html lang="en">
<head>
<meta charset="utf-8">
<title>Lend Aid – Business Card</title>
<link rel="stylesheet" href="https://fonts.googleapis.com/css2?family=Montserrat:wght@400;700&display=swap">
<style>
  :root {
    --bg: #2b2b2b;
    --card: #fbfbfa;
    --blue: #29a8e0;
    --green: #8cc63f;
    --text: #555a5e;
  }
  * { margin: 0; padding: 0; box-sizing: border-box; }
  html, body { width: 1200px; height: 1000px; overflow: hidden; }
  body {
    background: var(--bg);
    font-family: "Montserrat", Arial, sans-serif;
    display: flex;
    flex-direction: column;
    align-items: center;
    justify-content: space-evenly;
  }
  .card {
    position: relative;
    width: 760px;
    height: 434px;
    background: var(--card);
    border-radius: 14px;
    overflow: hidden;
    box-shadow: 0 10px 30px rgba(0,0,0,.45);
  }
  .brand {
    position: absolute;
    left: 60px;
    top: 60px;
    display: flex;
    align-items: center;
    gap: 14px;
  }
  .brand-mark {
    width: 46px;
    height: 46px;
    background: var(--blue);
    border-radius: 6px;
  }
  .brand-name {
    font-weight: 400;
    font-size: 46px;
    color: var(--blue);
    letter-spacing: .5px;
  }
  .decoration {
    position: absolute;
    right: -60px;
    top: -30px;
    width: 330px;
    height: 500px;
    border-radius: 40px;
    background: linear-gradient(160deg, var(--blue) 0%, #5cb8c9 55%, var(--green) 100%);
    opacity: .9;
  }
  .person {
    position: absolute;
    left: 60px;
    top: 230px;
  }
  .person-name {
    font-weight: 700;
    font-size: 26px;
    color: var(--green);
    letter-spacing: 1px;
    text-transform: uppercase;
  }
  .person-role {
    font-size: 19px;
    color: var(--text);
    margin-top: 4px;
  }
  .contact {
    position: absolute;
    left: 60px;
    bottom: 40px;
    list-style: none;
    font-size: 18px;
    color: var(--text);
  }
  .contact li {
    display: flex;
    align-items: center;
    gap: 12px;
    line-height: 30px;
  }
  .contact svg { width: 16px; height: 16px; fill: var(--blue); flex: none; }
</style>
</head>
<body>

  <section class="card card-back">
    <div class="brand">
      <span class="brand-mark"></span>
      <span class="brand-name">Lend Aid</span>
    </div>
    <div class="decoration" role="img" aria-label="Large brand decoration area in blue and green"></div>
  </section>

  <section class="card card-front">
    <div class="brand">
      <span class="brand-mark"></span>
      <span class="brand-name">Lend Aid</span>
    </div>
    <div class="decoration" role="img" aria-label="Large brand decoration area in blue and green"></div>

    <div class="person">
      <p class="person-name">Ria Vondeck</p>
      <p class="person-role">Customer Service Specialist</p>
    </div>

    <ul class="contact">
      <li>
        <svg viewBox="0 0 16 16" aria-hidden="true"><path d="M4 0h8a1 1 0 0 1 1 1v14a1 1 0 0 1-1 1H4a1 1 0 0 1-1-1V1a1 1 0 0 1 1-1zm1 2v10h6V2zm3 11a1 1 0 1 0 0 2 1 1 0 0 0 0-2z"/></svg>
        <span>+32491532876</span>
      </li>
      <li>
        <svg viewBox="0 0 16 16" aria-hidden="true"><path d="M0 3h16v10H0zm1.5 1.2L8 9l6.5-4.8V4H1.5z"/></svg>
        <span>ria.vondeck@lendaid.be</span>
      </li>
      <li>
        <svg viewBox="0 0 16 16" aria-hidden="true"><circle cx="8" cy="8" r="7.5"/></svg>
        <span>www.lendaid.be</span>
      </li>
    </ul>
  </section>

</body>
</html>
```